Fun Feminine Redesign Product Landing Page

This is our current product page
https://dovelmintery.com/product/coffee-substitute/

I like the overall feel of this but it needs to pop more. I love the pink an we are in the process of having illustrations made for the how to section.

Examples with more pop
https://www.brambleoven.com/products/chicken-bone-broth?shipping=8
https://pawtonmeal.com/products/lamb-turkey-kibble-grain-free

Target Market(s)

females 24-44

Number of Pages Required

1 page

Colors
0094D4
00A9DD
6FCCEA
C7EBF8
E9F6FB
00AB8E
00BBA5
67D7C9
C6EFE9
E9F9F6
FFC000
F8CF3A
FAE287
FDF2CF
FEFAEE
E54698
E96AAD
F1A4CE
F9D9EA
FCEFF6

Requirements
Must have
• Fresh, clean, feminine and unique

```html
<!DOCTYPE html>
<html lang="en">
<head>
<meta charset="utf-8">
<title>Original Coffee Substitute — Willowbrew</title>
<link href="https://fonts.googleapis.com/css2?family=Cormorant+Garamond:ital,wght@0,500;0,600;1,500;1,600&family=Jost:wght@300;400;500;600&display=swap" rel="stylesheet">
<style>
:root{
  --teal:#3f9e9b;
  --teal-dark:#2f7f7c;
  --teal-soft:#c6efe9;
  --pink-soft:#f9d9ea;
  --pink-wash:#fcefef;
  --coral:#ef7f72;
  --gold:#f8cf3a;
  --gold-soft:#fae287;
  --ink:#3b3b3b;
  --muted:#7c7c7c;
  --line:#e3e3e3;
  --white:#ffffff;
}
*{box-sizing:border-box;margin:0;padding:0}
html,body{width:1200px;height:3600px;overflow:hidden}
body{position:relative;background:var(--white);font-family:'Jost',sans-serif;color:var(--ink);font-size:13px}
.abs{position:absolute}

/* header */
.site-header{left:0;top:0;width:1200px;height:80px;background:var(--white);display:flex;align-items:center;padding:0 40px;justify-content:space-between}
.brand{display:flex;align-items:center;gap:8px;font-size:18px;font-weight:500;color:var(--teal-dark)}
.brand-dot{width:16px;height:16px;border-radius:50%;background:var(--gold)}
.main-nav{display:flex;gap:24px;align-items:center;font-size:13px}
.cart-btn{width:30px;height:30px;background:var(--teal);border-radius:4px;display:flex;align-items:center;justify-content:center}

/* hero */
.hero-band{left:0;top:80px;width:1200px;height:360px;background:var(--teal)}
.hero-leaf{left:30px;top:110px;width:200px;height:320px;border-radius:50% 50% 40% 60%;background:linear-gradient(160deg,rgba(255,255,255,.14),rgba(255,255,255,0))}
.product-shot{left:140px;top:100px;width:320px;height:500px;border-radius:10px;background:linear-gradient(170deg,#e98a55,#c8622f 70%,#b85528)}
.thumbs{left:150px;top:668px;display:flex;gap:16px}
.thumb{width:80px;height:80px;border-radius:4px;background:linear-gradient(160deg,#f1a77f,#c8622f);border:1px solid var(--line)}
.thumb.alt{background:linear-gradient(160deg,#f7f1ea,#d9cfc4)}
.thumb.alt2{background:linear-gradient(160deg,#f3dccd,#e7b89a)}
.product-title{left:732px;top:124px;width:400px;font-family:'Cormorant Garamond',serif;font-weight:600;font-size:42px;line-height:44px;color:var(--white)}
.rating{left:732px;top:220px;display:flex;gap:10px;align-items:center;color:var(--white);font-size:11px}
.stars{color:var(--gold);letter-spacing:2px;font-size:15px}
.hero-copy{left:732px;top:248px;width:420px;color:#e8f6f4;font-size:12px;line-height:1.55}
.hero-copy p+p{margin-top:10px}
.order-row{left:732px;top:488px;font-size:12px}
.order-row a{color:var(--coral)}
.price-boxes{left:732px;top:514px;display:flex;gap:10px}
.price-box{width:200px;height:58px;border:1px solid var(--line);border-radius:3px;padding:9px 12px;font-size:10px;color:var(--muted);background:var(--white)}
.price-box strong{display:block;color:var(--ink);font-weight:500;font-size:13px;margin-top:3px}
.price-box.on{border-color:var(--teal)}
.qty-label{left:732px;top:598px;font-size:12px}
.qty{left:732px;top:624px;display:flex;gap:10px}
.qty span{padding:8px 14px;border:1px solid var(--line);border-radius:3px;font-size:11px;background:var(--white)}
.qty span.on{border-color:var(--ink)}
.cart-row{left:732px;top:716px;display:flex;gap:12px}
.stepper{width:40px;height:36px;border:1px solid var(--line);border-radius:3px;display:flex;align-items:center;justify-content:center}
.add-cart{width:110px;height:36px;background:var(--coral);color:var(--white);border-radius:3px;font-size:12px;display:flex;align-items:center;justify-content:center}

/* goodness */
.goodness-bg{left:0;top:800px;width:1200px;height:600px;background:linear-gradient(180deg,#fff 0%,#fdf6f3 60%,var(--pink-wash) 100%)}
.section-title{width:1200px;left:0;text-align:center;font-family:'Cormorant Garamond',serif;font-weight:500;font-size:40px;line-height:48px;color:var(--teal-dark)}
.section-title em{font-style:italic;font-weight:600}
.title-rule{width:46px;height:2px;background:var(--teal);left:577px}
.ingredients-card{left:220px;top:980px;width:440px;height:400px;background:var(--white);border-radius:18px;box-shadow:0 8px 30px rgba(0,0,0,.07);padding:44px 56px}
.card-kicker{font-family:'Cormorant Garamond',serif;font-style:italic;color:var(--coral);font-size:32px;line-height:1}
.card-sub{font-size:16px;margin:6px 0 26px 24px}
.ing-list{list-style:none;font-size:13px;line-height:2.2}
.ing-list li::before{content:"•";color:var(--coral);margin-right:12px}
.facts-card{left:664px;top:1012px;width:384px;height:340px;background:var(--white);border:1px solid #f5cfc8;border-radius:18px;padding:44px 40px}
.facts-card .card-kicker{margin-bottom:22px}
.info-dot{right:26px;top:24px;width:24px;height:24px;border-radius:50%;background:var(--coral);color:#fff;font-size:13px;text-align:center;line-height:24px}
.fact{font-size:12px;line-height:1.55;margin-bottom:14px}
.fact b{font-weight:600}

/* how to */
.howto-bg{left:0;top:1400px;width:1200px;height:940px;background:var(--pink-wash)}
.step-circle{width:360px;height:360px;border-radius:50%;background:radial-gradient(circle at 45% 40%,#fff 0%,#fbf4f1 55%,#f6e6e1 100%)}
.step-art{width:280px;height:280px;border-radius:50%}
.step-name{width:360px;text-align:center;font-size:16px;letter-spacing:2px;color:var(--teal-dark);font-weight:500}
.step-text{width:300px;text-align:center;font-size:12px;line-height:1.6;color:var(--muted)}
.howto-note{left:0;width:1200px;top:2246px;text-align:center;font-size:12px;color:var(--muted)}

/* reasons */
.reasons-illus{left:320px;top:2396px;width:90px;height:80px;border-radius:50%;background:var(--pink-soft);opacity:.7}
.press-shot{left:220px;top:2560px;width:240px;height:440px;border-radius:8px;background:linear-gradient(180deg,#f4efea,#e0d2c4 55%,#6e4a33 100%)}
.check{left:528px;width:26px;height:26px;border-radius:3px;background:var(--gold);display:flex;align-items:center;justify-content:center}
.reason-card{left:576px;width:340px;background:var(--white);border-radius:4px;box-shadow:0 6px 24px rgba(0,0,0,.06);padding:14px 18px}
.reason-card h3{font-family:'Cormorant Garamond',serif;font-size:20px;font-weight:600;color:var(--teal-dark)}
.reason-card p{font-size:11px;line-height:1.55;color:var(--muted);margin-top:4px}

/* reviews */
.review-blob{left:450px;top:3026px;width:110px;height:90px;border-radius:50%;background:var(--gold-soft);opacity:.8}
.summary-score{left:60px;top:3180px;font-size:36px;font-weight:500;line-height:44px}
.summary-stars{left:132px;top:3184px}
.summary-based{left:132px;top:3206px;font-size:10px;color:var(--muted)}
.bars{left:320px;top:3180px}
.bar-row{display:flex;align-items:center;gap:6px;font-size:9px;color:var(--gold);margin-bottom:5px}
.bar{width:130px;height:9px;background:#eee}
.bar i{display:block;height:9px;background:var(--gold)}
.bar-count{color:var(--muted)}
.review-actions{left:880px;top:3200px;display:flex;gap:10px}
.review-actions span{border:1px solid var(--line);padding:7px 14px;font-size:10px;color:var(--muted)}
.tabs{left:60px;top:3330px;width:1080px;border-bottom:1px solid var(--line);display:flex;gap:26px;font-size:11px;padding-bottom:8px}
.tabs .on{border-bottom:2px solid var(--ink);padding-bottom:7px;margin-bottom:-9px}
.review-item{left:60px;top:3372px;width:1080px;height:120px}
.avatar{width:38px;height:38px;border-radius:50%;background:var(--teal-soft)}
.review-head{display:flex;gap:10px;align-items:center;font-size:11px}
.verified{color:var(--teal);font-size:9px}
.review-title{font-family:'Cormorant Garamond',serif;font-size:22px;font-weight:600;margin-top:14px}
.review-body{font-size:11px;color:var(--muted);margin-top:4px}
.review-foot{right:0;top:4px;font-size:10px;color:var(--muted)}
.fade-foot{left:0;top:3520px;width:1200px;height:80px;background:linear-gradient(180deg,rgba(255,255,255,0),#e9e9e9)}
</style>
</head>
<body>

<header class="abs site-header">
  <div class="brand"><span class="brand-dot"></span>Willowbrew</div>
  <nav class="main-nav">
    <span>About</span><span>How to Brew</span><span>Wholesale</span><span>Shop</span><span>Content</span><span>FAQ</span><span>Account Login</span><span>Retailers</span>
    <span class="cart-btn"><svg width="14" height="14" viewBox="0 0 24 24" fill="none" stroke="#fff" stroke-width="2"><path d="M3 4h3l2 11h11l2-8H7"/><circle cx="9" cy="20" r="1.5"/><circle cx="18" cy="20" r="1.5"/></svg></span>
  </nav>
</header>

<section aria-label="Product">
  <div class="abs hero-band"></div>
  <div class="abs hero-leaf"></div>
  <div class="abs product-shot" role="img" aria-label="Orange pouch of Original Coffee Substitute"></div>
  <div class="abs thumbs">
    <div class="thumb" role="img" aria-label="Pouch front view"></div>
    <div class="thumb alt" role="img" aria-label="Pouch back label"></div>
    <div class="thumb alt2" role="img" aria-label="Cup of brewed substitute"></div>
  </div>
  <h1 class="abs product-title">Original Coffee<br>Substitute</h1>
  <div class="abs rating"><span class="stars">★★★★★</span><span>Based on 6 reviews</span></div>
  <div class="abs hero-copy">
    <p>The blend that started it all… Original Willowbrew will become your go-to beverage when you're trying to replace that classic cup of joe.</p>
    <p>It has a gentle flavor — not burnt, never acidic, it has just the right natural tinge of bitterness.</p>
  </div>
  <div class="abs order-row">One-time order or <a>Subscribe and Save</a></div>
  <div class="abs price-boxes">
    <div class="price-box on">One-time order<strong>$12.00 — $38.00</strong></div>
    <div class="price-box">Subscribe<strong>$10.20 — $32.30 / month</strong></div>
  </div>
  <div class="abs qty-label">Choose quantity</div>
  <div class="abs qty"><span class="on">4 oz (14 servings)</span><span>8 oz (30 servings)</span></div>
  <div class="abs cart-row"><div class="stepper">1</div><div class="add-cart">Add to Cart</div></div>
</section>

<section aria-label="Ingredients">
  <div class="abs goodness-bg"></div>
  <h2 class="abs section-title" style="top:848px">The <em>goodness</em> inside</h2>
  <div class="abs title-rule" style="top:904px"></div>
  <div class="abs ingredients-card">
    <div class="card-kicker">Really…</div>
    <div class="card-sub">that's the full ingredient list!</div>
    <ul class="ing-list">
      <li>Organic Roasted Chicory Root</li>
      <li>Organic Roasted Carob Powder</li>
      <li>Organic Roasted Dandelion Powder</li>
      <li>Maple Sugar</li>
      <li>Date Sugar</li>
      <li>Ground Vanilla Beans</li>
      <li>Sea Salt</li>
    </ul>
  </div>
  <div class="abs facts-card">
    <div class="abs info-dot">i</div>
    <div class="card-kicker">Did you know?</div>
    <p class="fact"><b>Chicory root's</b> components have been found to work as antioxidants and anti-inflammatories.</p>
    <p class="fact"><b>Carob</b> has twice the calcium of cocoa.</p>
    <p class="fact"><b>Dandelion</b> contains both beta-carotene, and polyphenols which work against oxidative stress in your body.</p>
  </div>
</section>

<section aria-label="How to brew">
  <div class="abs howto-bg"></div>
  <h2 class="abs section-title" style="top:1568px">How to make the <em>perfect cup</em></h2>
  <div class="abs title-rule" style="top:1624px"></div>

  <div class="abs step-circle" style="left:60px;top:1656px"></div>
  <div class="abs step-art" style="left:100px;top:1696px;background:radial-gradient(circle,#c6efe9 0%,rgba(63,158,155,.35) 60%,rgba(255,255,255,0) 70%)" role="img" aria-label="Illustration of measuring a spoonful into a filter"></div>
  <div class="abs step-name" style="left:60px;top:2060px">MEASURE</div>
  <p class="abs step-text" style="left:90px;top:2090px">Place 1 tsp of Willowbrew in a coffee filter or single-cup brew bag, per 8 oz of water.</p>

  <div class="abs step-circle" style="left:420px;top:1656px"></div>
  <div class="abs step-art" style="left:460px;top:1696px;background:radial-gradient(circle,#f9d9ea 0%,rgba(239,127,114,.3) 60%,rgba(255,255,255,0) 70%)" role="img" aria-label="Illustration of a french press and kettle"></div>
  <div class="abs step-name" style="left:420px;top:2060px">PREP</div>
  <p class="abs step-text" style="left:450px;top:2090px">Place 1 tsp of Willowbrew in a coffee press or single-cup brew bag. Pour in hot water over it.</p>

  <div class="abs step-circle" style="left:780px;top:1656px"></div>
  <div class="abs step-art" style="left:820px;top:1696px;background:radial-gradient(circle,#c6efe9 0%,rgba(47,127,124,.35) 60%,rgba(255,255,255,0) 70%)" role="img" aria-label="Illustration of a pour-over cup steeping"></div>
  <div class="abs step-name" style="left:780px;top:2060px">STEEP</div>
  <p class="abs step-text" style="left:810px;top:2090px">Let it steep for 3 to 5 minutes, then remove the filter and enjoy your warm cup.</p>

  <p class="abs howto-note">*Want a stronger flavor? Let it steep longer. OR use a higher ratio of powder to water.</p>
</section>

<section aria-label="Reasons">
  <div class="abs reasons-illus" role="img" aria-label="Pink floral sketch"></div>
  <h2 class="abs section-title" style="top:2436px">Pour on the <em>reasons</em> you'll <em style="color:var(--coral)">love it</em></h2>
  <div class="abs press-shot" role="img" aria-label="French press of brewed substitute with a wooden spoon"></div>

  <div class="abs check" style="top:2590px"><svg width="14" height="14" viewBox="0 0 24 24" fill="none" stroke="#fff" stroke-width="3"><path d="M4 12l5 5L20 6"/></svg></div>
  <div class="abs reason-card" style="top:2572px"><h3>None of the Junk</h3><p>No added or even hidden "natural" flavors.</p></div>

  <div class="abs check" style="top:2698px"><svg width="14" height="14" viewBox="0 0 24 24" fill="none" stroke="#fff" stroke-width="3"><path d="M4 12l5 5L20 6"/></svg></div>
  <div class="abs reason-card" style="top:2676px"><h3>Minerals Galore</h3><p>Seed to cup herbal harvest: our roots and carob are rich with calcium, copper, magnesium, iron, zinc and more.</p></div>

  <div class="abs check" style="top:2814px"><svg width="14" height="14" viewBox="0 0 24 24" fill="none" stroke="#fff" stroke-width="3"><path d="M4 12l5 5L20 6"/></svg></div>
  <div class="abs reason-card" style="top:2792px"><h3>Good for the Gut</h3><p>Chicory, carob and dandelion are naturally prebiotic fiber, which feed the good bacteria in your belly.</p></div>
</section>

<section aria-label="Reviews">
  <div class="abs review-blob"></div>
  <h2 class="abs section-title" style="top:3060px">Read Our Reviews</h2>
  <div class="abs summary-score">4.8</div>
  <div class="abs summary-stars stars">★★★★★</div>
  <div class="abs summary-based">Based on 6 Reviews</div>
  <div class="abs bars">
    <div class="bar-row">★★★★★<span class="bar"><i style="width:84%"></i></span><span class="bar-count">5</span></div>
    <div class="bar-row">★★★★☆<span class="bar"><i style="width:16%"></i></span><span class="bar-count">1</span></div>
    <div class="bar-row">★★★☆☆<span class="bar"><i style="width:0"></i></span><span class="bar-count">0</span></div>
    <div class="bar-row">★★☆☆☆<span class="bar"><i style="width:0"></i></span><span class="bar-count">0</span></div>
    <div class="bar-row">★☆☆☆☆<span class="bar"><i style="width:0"></i></span><span class="bar-count">0</span></div>
  </div>
  <div class="abs review-actions"><span>Ask a Question</span><span>Write a Review</span></div>
  <div class="abs tabs"><span class="on">Reviews (6)</span><span>Questions (1)</span></div>
  <article class="abs review-item">
    <div class="review-head"><div class="avatar"></div><div>Rachel M. <span class="verified">Verified Buyer</span><br><span class="stars" style="font-size:11px">★★★★☆</span></div></div>
    <div class="review-title">Very Good</div>
    <p class="review-body">I needed to quit coffee and this helped a lot. Smooth taste, no jitters at all.</p>
    <div class="abs review-foot">Was this helpful? 0 · 0</div>
  </article>
  <div class="abs fade-foot"></div>
</section>

</body>
</html>
```